MODELS AGENCY NEW YEAR 2026 CARD

A 10 cm x 21 cm horizontal New Year card for clients of our 2 models agencies, Pommelin (kids) and Velvaride (actors and adults) (logo in the jobs).

Side A of the card: creative mission:
-text: 2026
-text: Peace and Love
-Studio or movie set atmosphere
-tone of voice: optimistic, positive, colorful

Side B:
(name of 4 people of the agency:)
Odette, Anne-Sophie, Hortense & Luc-Antoine,
(2 logos)
Pommelin & VelvaRide
(Adres)
Rue des Tilleuls 74 b3 - 1200 Bruxelles - Belgique

Target Market(s)

Movie directors, photographers

Industry/Entity Type

Fashion, advertising & Movies

Requirements
Must have
• SEE TEXT IN BRIEFING

```html
<!DOCTYPE html>
<html lang="fr">
<head>
<meta charset="utf-8">
<title>Pommelin &amp; VelvaRide — Carte de vœux 2026</title>
<link rel="stylesheet" href="https://fonts.googleapis.com/css2?family=League+Spartan:wght@400;700&family=Outfit:wght@800&family=Playfair+Display:wght@400&display=swap">
<style>
  :root {
    --paper: #ffffff;
    --ink-dark: #0c0b0a;
    --ink-brown: #3b2c1f;
    --white: #ffffff;
    --gold: #f3cc5a;
    --gold-light: #fbe46e;
    --gold-mid: #e2a93a;
    --gold-deep: #b87325;
    --photo-grey: #8c857d;
    --photo-light: #e9e7e3;
  }
  * { box-sizing: border-box; margin: 0; padding: 0; }
  html, body { width: 1200px; height: 1200px; overflow: hidden; background: var(--paper); }
  .canvas { position: relative; width: 1200px; height: 1200px; }

  .card {
    position: absolute; left: 114px; width: 981px; height: 467px; overflow: hidden;
    background: linear-gradient(90deg, var(--ink-dark) 0%, #15110e 35%, #2a1f17 65%, var(--ink-brown) 100%);
  }
  .card--front { top: 120px; }
  .card--back { top: 621px; }

  .brand { position: absolute; font-family: "League Spartan", sans-serif; color: var(--white); }
  .brand__name { font-weight: 700; font-size: 34px; line-height: 1; letter-spacing: 1px; }
  .brand__tagline { font-weight: 400; font-size: 9.5px; letter-spacing: 1.6px; margin-top: 6px; text-transform: uppercase; }
  .brand--center { text-align: center; }

  .card--front .brand--adults { left: 54px; top: 68px; }
  .card--front .brand--kids { left: 282px; top: 66px; width: 210px; }
  .card--back .brand--adults { left: 80px; top: 45px; }
  .card--back .brand--kids { left: 277px; top: 43px; width: 175px; }
  .card--back .brand__name { font-size: 30px; }
  .card--back .brand__tagline { font-size: 8.5px; }

  .greeting {
    position: absolute; left: 52px; top: 158px;
    font-family: "Playfair Display", serif; font-weight: 400; color: var(--white);
    font-size: 122px; line-height: 126px; letter-spacing: -1px;
  }

  .wave, .year { position: absolute; left: 0; top: 0; }

  .team {
    position: absolute; left: 80px; top: 130px;
    font-family: "League Spartan", sans-serif; font-weight: 700; font-size: 47px; line-height: 58px;
    color: var(--white); list-style: none; text-transform: uppercase;
  }
  .team__name--accent { color: var(--gold); }

  .address {
    position: absolute; left: 80px; top: 401px;
    font-family: "League Spartan", sans-serif; font-weight: 700; font-size: 16.5px; color: var(--white);
  }

  .portrait {
    position: absolute; right: 0; top: 0; width: 420px; height: 467px;
    background: linear-gradient(90deg, rgba(59,44,31,0) 0%, rgba(110,96,82,0.55) 30%, var(--photo-grey) 55%, var(--photo-light) 100%);
  }
</style>
</head>
<body>
<main class="canvas">

  <section class="card card--front" aria-label="Recto : Peace &amp; Love 2026">
    <svg class="wave" width="981" height="467" viewBox="0 0 981 467" aria-hidden="true">
      <defs>
        <linearGradient id="gold-band" x1="0" y1="0" x2="1" y2="0">
          <stop offset="0" stop-color="var(--gold-light)"/>
          <stop offset="0.35" stop-color="var(--gold-deep)"/>
          <stop offset="0.65" stop-color="var(--gold-light)"/>
          <stop offset="1" stop-color="var(--gold-deep)"/>
        </linearGradient>
        <linearGradient id="gold-digit" x1="0" y1="0" x2="1" y2="1">
          <stop offset="0" stop-color="var(--gold-light)"/>
          <stop offset="0.5" stop-color="var(--gold-mid)"/>
          <stop offset="1" stop-color="var(--gold-deep)"/>
        </linearGradient>
        <radialGradient id="digit-shadow" cx="0.5" cy="0.5" r="0.5">
          <stop offset="0" stop-color="#000" stop-opacity="0.7"/>
          <stop offset="1" stop-color="#000" stop-opacity="0"/>
        </radialGradient>
      </defs>
      <path d="M555,0 C650,28 720,40 790,39 C870,38 930,20 981,0 Z" fill="url(#gold-band)"/>
      <path d="M0,458 C80,440 160,420 236,420 C340,420 440,449 530,449 C610,449 690,424 761,424 C850,424 920,436 981,446 L981,467 L0,467 Z" fill="url(#gold-band)"/>
      <ellipse cx="740" cy="388" rx="150" ry="10" fill="url(#digit-shadow)"/>
      <g class="year" font-family="Outfit, sans-serif" font-weight="800" fill="url(#gold-digit)" stroke="var(--gold-deep)" stroke-width="3">
        <text x="583" y="267" font-size="270" textLength="246" lengthAdjust="spacingAndGlyphs">20</text>
        <text x="677" y="361" font-size="270" textLength="221" lengthAdjust="spacingAndGlyphs">26</text>
      </g>
    </svg>

    <div class="brand brand--adults">
      <div class="brand__name">VelvaRide</div>
      <div class="brand__tagline">People actors &amp; models agency</div>
    </div>
    <div class="brand brand--kids brand--center">
      <div class="brand__name">Pommelin</div>
      <div class="brand__tagline">Children models agency</div>
    </div>

    <h1 class="greeting">Peace &amp;<br>Love</h1>
  </section>

  <section class="card card--back" aria-label="Verso : l'équipe de l'agence">
    <div class="portrait" role="img" aria-label="Photo noir et blanc d'une membre de l'équipe assise dans un fauteuil avec un ordinateur portable"></div>

    <div class="brand brand--adults">
      <div class="brand__name">VelvaRide</div>
      <div class="brand__tagline">People actors &amp; models agency</div>
    </div>
    <div class="brand brand--kids brand--center">
      <div class="brand__name">Pommelin</div>
      <div class="brand__tagline">Children models agency</div>
    </div>

    <ul class="team">
      <li class="team__name team__name--accent">Odette</li>
      <li class="team__name">Anne-Sophie</li>
      <li class="team__name team__name--accent">Hortense</li>
      <li class="team__name">Luc-Antoine</li>
    </ul>

    <p class="address">Rue des Tilleuls 74 b3 - 1200 Bruxelles - Belgique</p>
  </section>

</main>
</body>
</html>
```